TovaLamarpe - Israeli Mental Health Website

We are developing an Israeli website for mental health. The website will be both in English and in Hebrew. We have a logo and would like a website design based on the logo and the logos colors (attached).

Attached is a doc that contains the website requirements.

We would like to have an icon for each of the sidebar categories, an image for each of the pages (including each of the sidebar category pages).

Target Market(s)

Adults 18-80

Industry/Entity Type

Mental Health

Number of Pages Required

5+ page

Font styles to use
Sans Serif

Colors

Designer to choose colors to be used in the design.

```html
<!DOCTYPE html>
<html lang="en">
<head>
<meta charset="utf-8">
<title>TovaLamarpe – Mental Health</title>
<link href="https://fonts.googleapis.com/css2?family=Roboto:wght@400;500;700&display=swap" rel="stylesheet">
<style>
:root{
  --blue:#1f6fbd;
  --green:#4aa83c;
  --navy:#0f2f4d;
  --footer:#0c3d78;
  --text:#555a60;
  --light:#f4f5f7;
  --white:#ffffff;
}
*{margin:0;padding:0;box-sizing:border-box}
html,body{width:1200px;height:3456px;overflow:hidden}
body{position:relative;font-family:'Roboto',sans-serif;background:var(--white);color:var(--navy)}
.abs{position:absolute}
.btn{position:absolute;display:flex;align-items:center;justify-content:center;border-radius:30px;font-weight:500;font-size:19px;color:var(--white);white-space:nowrap}
.btn-blue{background:var(--blue)}
.btn-green{background:var(--green)}
.btn-white{background:var(--white);color:var(--navy)}
.eyebrow{position:absolute;color:var(--green);font-size:19px;text-transform:uppercase}
.heading{position:absolute;font-size:37px;font-weight:500;text-transform:uppercase;color:#141a22;white-space:nowrap}
.body-text{position:absolute;font-size:15px;line-height:22.5px;color:var(--text)}
.photo{position:absolute;border-radius:12px}

/* header */
.site-header{position:absolute;left:0;top:0;width:1200px;height:94px;background:var(--white);border-bottom:1px solid #e6e6e6}
.brand{position:absolute;left:112px;top:26px;display:flex;align-items:center;gap:10px;font-size:24px;font-weight:700;color:var(--blue)}
.brand-dot{width:34px;height:34px;border-radius:50%;background:var(--green)}
.nav{position:absolute;top:42px;font-size:14px;color:#1b1b1b}
.nav span{position:absolute;white-space:nowrap}
.donate{left:969px;top:30px;width:118px;height:36px;font-size:14px;gap:8px}

/* hero */
.hero{position:absolute;left:0;top:94px;width:1200px;height:587px;background:linear-gradient(180deg,#9fb6c0 0%,#b9c3a8 35%,#c9a64a 62%,#6b6a3a 100%)}
.hero-title{position:absolute;left:0;width:1200px;top:282px;text-align:center;color:var(--white);font-weight:700;font-size:60px;line-height:62px}
.hero-sub{position:absolute;left:0;width:1200px;top:428px;text-align:center;color:var(--white);font-size:15px;font-weight:500}

/* emergency */
.sea{position:absolute;left:0;top:1109px;width:1200px;height:492px;background:linear-gradient(180deg,#ffffff 0%,#d9ecf2 12%,#7fc0cf 40%,#6bb5c4 70%,#a8d6dc 100%)}
.help-card{position:absolute;left:114px;top:1174px;width:973px;height:360px;background:var(--white);border-radius:12px}

/* specialty */
.specialty{position:absolute;left:0;top:1601px;width:1200px;height:573px;background:var(--light)}
.card{position:absolute;top:1766px;width:311px;height:344px;background:var(--white);border-radius:8px;overflow:hidden}
.card-photo{position:absolute;left:0;top:0;width:311px;height:196px}
.card-icon{position:absolute;left:118px;top:160px;width:74px;height:74px;border-radius:50%;background:var(--white);display:flex;align-items:center;justify-content:center}
.card-title{position:absolute;left:0;top:238px;width:311px;text-align:center;font-size:12.5px;font-weight:500;color:#111}
.card-text{position:absolute;left:45px;top:264px;width:221px;text-align:center;font-size:10px;line-height:14.5px;color:#777}

/* video */
.video{position:absolute;left:0;top:2174px;width:1200px;height:404px;background:linear-gradient(180deg,#3f7fc0 0%,#2e6fb5 45%,#4d8fc9 80%,#8fb8d8 100%)}

/* testimonial */
.t-card{position:absolute;top:2687px;width:231px;height:299px;background:var(--white);border-radius:6px;box-shadow:0 2px 10px rgba(0,0,0,.08);overflow:hidden}
.t-photo{position:absolute;left:0;top:0;width:231px;height:241px}
.t-name{position:absolute;left:0;top:262px;width:231px;text-align:center;font-size:13px;color:#111}

/* cta */
.cta{position:absolute;left:0;top:3029px;width:1200px;height:153px;background:var(--green)}

/* footer */
.footer{position:absolute;left:0;top:3182px;width:1200px;height:274px;background:var(--footer);color:var(--white)}
.social{position:absolute;top:3362px;width:40px;height:40px;border:2px solid var(--white);border-radius:50%}
</style>
</head>
<body>

<header class="site-header">
  <div class="brand"><span class="brand-dot"></span>TovaLamarpe</div>
  <nav class="nav">
    <span style="left:393px">Smart Chatline</span>
    <span style="left:520px">Therapists</span>
    <span style="left:616px">Organizations</span>
    <span style="left:736px">Videos</span>
    <span style="left:816px">Contact</span>
    <span style="left:895px">About</span>
  </nav>
  <div class="btn btn-green donate">
    <svg width="16" height="14" viewBox="0 0 16 14"><path d="M8 13 L1.5 6.5 A3.5 3.5 0 0 1 8 2 A3.5 3.5 0 0 1 14.5 6.5 Z" fill="#fff"/></svg>Donate
  </div>
</header>

<section class="hero" role="img" aria-label="Woman with arms open in a field of yellow flowers under a soft sky"></section>
<h1 class="hero-title">Find Hope For<br>The Journey Ahead</h1>
<p class="hero-sub">Compassionate Counseling Services From Delaware's Grief And Trauma Therapists</p>
<div class="btn btn-blue" style="left:468px;top:475px;width:263px;height:48px;font-size:15px">Start Your Healing Journey</div>

<!-- about -->
<p class="eyebrow" style="left:112px;top:740px">Mental Health</p>
<h2 class="heading" style="left:112px;top:772px">About Us</h2>
<p class="body-text" style="left:112px;top:835px;width:495px">Lorem ipsum dolor sit amet, consectetur adipiscing elit, sed do eiusmod tempor incididunt ut labore et dolore magna aliqua. Ut enim ad minim veniam, quis nostrud exercitation ullamco laboris nisi ut aliquip ex ea commodo consequat. Duis aute irure dolor in reprehenderit in voluptate velit esse cillum dolore eu fugiat nulla pariatur.<br><br>Excepteur sint occaecat cupidatat non proident, sunt in culpa qui officia deserunt mollit anim id est laborum.</p>
<div class="btn btn-blue" style="left:113px;top:1056px;width:177px;height:47px">Learn More</div>
<div class="photo" role="img" aria-label="Counselor talking with a couple in a bright office" style="left:653px;top:741px;width:434px;height:368px;background:linear-gradient(135deg,#c9ccd0,#8a7a6a 55%,#3c3f52)"></div>

<!-- emergency -->
<div class="sea" role="img" aria-label="Calm turquoise sea under a pale sky"></div>
<div class="help-card"></div>
<div class="photo" role="img" aria-label="Therapist taking notes while a client rests on a sofa" style="left:170px;top:1229px;width:292px;height:249px;background:linear-gradient(135deg,#2f3438,#c88a3a 45%,#8fa3b8)"></div>
<p class="eyebrow" style="left:527px;top:1225px">Mental Health</p>
<h2 class="heading" style="left:526px;top:1258px">Emergency Mental Help</h2>
<p class="body-text" style="left:527px;top:1313px;width:475px">Lorem ipsum dolor sit amet, consectetur adipiscing elit, sed do eiusmod tempor incididunt ut labore et dolore magna aliqua. Ut enim ad minim veniam, quis nostrud exercitation ullamco laboris nisi ut aliquip ex ea commodo consequat.</p>
<div class="btn btn-blue" style="left:528px;top:1428px;width:186px;height:47px">Book A Session</div>
<div class="btn btn-green" style="left:734px;top:1428px;width:231px;height:47px">Join Our Community</div>

<!-- specialty -->
<section class="specialty"></section>
<p class="eyebrow" style="left:0;width:1213px;text-align:center;top:1651px">What We Provide</p>
<h2 class="heading" style="left:0;width:1213px;text-align:center;top:1686px">Areas Of Specialty Are</h2>
<svg class="abs" style="left:52px;top:1914px" width="24" height="16" viewBox="0 0 24 16"><path d="M23 8H2M8 2L2 8l6 6" stroke="#1f6fbd" stroke-width="2" fill="none"/></svg>
<svg class="abs" style="left:1125px;top:1914px" width="24" height="16" viewBox="0 0 24 16"><path d="M1 8h21M16 2l6 6-6 6" stroke="#1f6fbd" stroke-width="2" fill="none"/></svg>

<article class="card" style="left:113px">
  <div class="card-photo" role="img" aria-label="Doctor in a white coat speaking with a patient" style="background:linear-gradient(135deg,#5a4a3e,#c9c2b8 50%,#7b7f86)"></div>
  <div class="card-icon"><svg width="30" height="30" viewBox="0 0 30 30" fill="none" stroke="#3aa0a8" stroke-width="1.6"><circle cx="10" cy="9" r="4"/><circle cx="20" cy="9" r="4"/><path d="M3 26v-5a5 5 0 0 1 5-5h4a5 5 0 0 1 5 5v5M17 16h5a5 5 0 0 1 5 5v5"/></svg></div>
  <h3 class="card-title">THERAPISTS</h3>
  <p class="card-text">Lorem ipsum dolor sit amet, consectetur adipiscing elit, sed do eiusmod tempor incididunt ut labore et dolore magna aliqua.</p>
</article>
<article class="card" style="left:445px">
  <div class="card-photo" role="img" aria-label="Woman smiling at her phone in a warm lit living room" style="background:linear-gradient(135deg,#2b2620,#b08a5e 55%,#4a3d30)"></div>
  <div class="card-icon"><svg width="30" height="30" viewBox="0 0 30 30" fill="none" stroke="#3aa0a8" stroke-width="1.6"><path d="M15 5a7 7 0 0 0-4 12.7V21h8v-3.3A7 7 0 0 0 15 5z"/><path d="M12 24h6M15 1v2M4 12H2M28 12h-2M6 4l1.5 1.5M24 4l-1.5 1.5"/></svg></div>
  <h3 class="card-title">SMART CHATLINE</h3>
  <p class="card-text">Lorem ipsum dolor sit amet, consectetur adipiscing elit, sed do eiusmod tempor incididunt ut labore et dolore magna aliqua.</p>
</article>
<article class="card" style="left:777px">
  <div class="card-photo" role="img" aria-label="Group of women talking around a table in an office" style="background:linear-gradient(135deg,#8a5a44,#d8d2cc 50%,#6a4f8a)"></div>
  <div class="card-icon"><svg width="30" height="30" viewBox="0 0 30 30" fill="none" stroke="#3aa0a8" stroke-width="1.6"><circle cx="15" cy="13" r="10"/><circle cx="15" cy="11" r="3"/><path d="M9 20a6 6 0 0 1 12 0M10 27h10"/></svg></div>
  <h3 class="card-title">ORGANIZATIONS</h3>
  <p class="card-text">Lorem ipsum dolor sit amet, consectetur adipiscing elit, sed do eiusmod tempor incididunt ut labore et dolore magna aliqua.</p>
</article>

<!-- video -->
<section class="video" role="img" aria-label="Blue ocean beneath palm leaves"></section>
<div class="photo" role="img" aria-label="Man meditating cross-legged outside a modern building" style="left:114px;top:2230px;width:396px;height:286px;background:linear-gradient(135deg,#6b7a86,#c8c0b2 50%,#4d5a66)"></div>
<svg class="abs" style="left:292px;top:2354px" width="40" height="40" viewBox="0 0 40 40"><circle cx="20" cy="20" r="19" fill="rgba(255,255,255,.55)"/><path d="M16 12l12 8-12 8z" fill="#fff"/></svg>
<h2 class="heading" style="left:588px;top:2256px;color:#fff;font-size:38px">Our Video Sessions</h2>
<p class="body-text" style="left:589px;top:2325px;width:440px;color:#fff">Lorem ipsum dolor sit amet, consectetur adipiscing elit, sed do eiusmod tempor incididunt ut labore et dolore magna aliqua.Ut enim ad minim veniam, quis nostrud exercitation ullamco laboris nisi ut aliquip ex ea commodo consequat.</p>
<div class="btn btn-white" style="left:590px;top:2440px;width:182px;height:48px">Watch Videos</div>
<div class="btn btn-green" style="left:782px;top:2440px;width:186px;height:48px">Book A Session</div>

<!-- testimonial -->
<h2 class="heading" style="left:0;width:1204px;text-align:center;top:2616px;color:var(--navy)">Testimonial</h2>
<article class="t-card" style="left:113px"><div class="t-photo" role="img" aria-label="Portrait of a man in a navy suit" style="background:linear-gradient(180deg,#6a5a50,#1f2a44)"></div><p class="t-name">DANIEL R. HOLLIS,LCSW</p></article>
<article class="t-card" style="left:361px"><div class="t-photo" role="img" aria-label="Portrait of a smiling woman in a grey blazer" style="background:linear-gradient(180deg,#8e8a86,#b9b6b2)"></div><p class="t-name">DANIEL R. HOLLIS,LCSW</p></article>
<article class="t-card" style="left:608px"><div class="t-photo" role="img" aria-label="Portrait of a man in a grey suit" style="background:linear-gradient(180deg,#9aa3ad,#585e66)"></div><p class="t-name">DANIEL R. HOLLIS,LCSW</p></article>
<article class="t-card" style="left:854px"><div class="t-photo" role="img" aria-label="Portrait of a smiling woman among red leaves" style="background:linear-gradient(180deg,#9a2a3a,#3a1a22)"></div><p class="t-name">DANIEL R. HOLLIS,LCSW</p></article>

<!-- call to action -->
<section class="cta"></section>
<h2 class="abs" style="left:169px;top:3059px;color:#fff;font-size:36px;font-weight:700">Ready For Innovation?</h2>
<p class="abs" style="left:171px;top:3111px;width:490px;color:#fff;font-size:15px;line-height:22px">Lorem ipsum dolor sit amet, consectetur adipiscing elit. Mauris sapien eros, consequat vel eros ac, volutpat bibendum massa.</p>
<div class="btn btn-white" style="left:836px;top:3075px;width:234px;height:56px;color:var(--blue);font-weight:400">GET IN TOUCH</div>

<!-- footer -->
<footer class="footer"></footer>
<div class="abs" style="left:112px;top:3278px;display:flex;align-items:center;gap:10px;color:#fff;font-size:26px;font-weight:700"><span style="width:30px;height:30px;border-radius:50%;background:#fff"></span>TovaLamarpe</div>
<p class="abs" style="left:112px;top:3326px;color:#fff;font-size:12px;font-weight:500">Organization for Mental Health ©2023</p>
<span class="social" style="left:114px"></span>
<span class="social" style="left:164px"></span>
<span class="social" style="left:215px"></span>
<span class="social" style="left:265px"></span>

<h3 class="abs" style="left:376px;top:3218px;color:#fff;font-size:23px;font-weight:500">Contact</h3>
<p class="abs" style="left:376px;top:3265px;color:#fff;font-size:14.5px;line-height:22.5px">418 Cedar Hollow Ave., Ste 12<br>Milford, DE, 19963<br>Phone: (555) 214-7730<br>FAX: (555) 214-7731</p>
<p class="abs" style="left:590px;top:3221px;color:#fff;font-size:14.5px;line-height:22px">Home<br>About us<br>Service<br>Form</p>

<h3 class="abs" style="left:729px;top:3218px;color:#fff;font-size:28px;font-weight:500;white-space:nowrap">Subscribe To Our Newsletter</h3>
<div class="abs" style="left:729px;top:3265px;width:355px;height:47px;border:1.5px solid #fff;border-radius:24px;color:#fff;font-size:14px;padding:15px 30px">Enter your email</div>
<div class="btn btn-white" style="left:729px;top:3331px;width:179px;height:48px">Subscribe</div>

</body>
</html>
```